Cover art needed for best LASIK patient education book ever written!

Help us design a an outstanding cover for this book:
Three Lamps at Dusk?
Quiet Pointers for Picking a Trustworthy Retina Practitioner
By Derek H. Tolland, MD and
Glen T. Ashworth
We give you nine chapters of easy-to-understand explanations about how LASIK may, or may not, help improve you vision. In addition, we offer tell-all secrets and insider tips on how to tell whether the LASIK center is doing what is best for your vision, or for their financial performance. If you have ever considered LASIK laser vision correction, this book is required reading before you make a decision.
So what do you say? Will you draw a great cover for our book? By the way, preferred colors include jewel tones like deep purple and royal blue.
Target Market(s)
graphic designers
Industry/Entity Type
Medical
Requirements
Must have
- Book Title
- Subtitle
- Outstanding Graphics
- Derek H. Tolland, MD (main author) should be in slightly larger font than Glen T. Ashworth (secondary author)
- compelling art that makes you want to pick up the book
Should not have
- no blood, image representing pain, or anything else that would generally not appeal to patients

```html
<!DOCTYPE html>
<html lang="en">
<head>
<meta charset="utf-8">
<title>Three Lamps at Dusk? — Book Cover</title>
<link href="https://fonts.googleapis.com/css2?family=Jost:wght@400;500;600;700&display=swap" rel="stylesheet">
<style>
  :root {
    --page: #e9e6e3;
    --cover: #141414;
    --ink-light: #f4e9ec;
    --royal-blue: #1e93d6;
    --deep-purple: #9c4aa8;
    --eye-shadow: #050505;
  }
  html, body {
    margin: 0;
    width: 1200px;
    height: 1200px;
    overflow: hidden;
    background: var(--page);
  }
  .cover {
    position: absolute;
    left: 206px;
    top: 20px;
    width: 788px;
    height: 1160px;
    background: var(--cover);
    font-family: "Jost", sans-serif;
    color: var(--ink-light);
    box-shadow: 0 6px 24px rgba(0,0,0,0.25);
  }
  .title-row {
    position: absolute;
    left: 0;
    width: 100%;
    display: flex;
    justify-content: center;
    align-items: center;
    gap: 10px;
    height: 122px;
  }
  .title-word {
    font-weight: 400;
    font-size: 166px;
    line-height: 1;
    letter-spacing: 0.06em;
    text-transform: uppercase;
  }
  .eye-art {
    width: 118px;
    height: 118px;
    flex: none;
  }
  .subtitle-line {
    position: absolute;
    left: 0;
    width: 100%;
    text-align: center;
    font-weight: 700;
    font-size: 21px;
    letter-spacing: 0.5em;
    text-indent: 0.5em;
    color: var(--royal-blue);
    text-transform: uppercase;
    line-height: 1;
  }
  .subtitle-line.accent { color: var(--deep-purple); }
  .question-mark {
    position: absolute;
    left: 0;
    width: 100%;
    top: 872px;
    text-align: center;
    font-weight: 600;
    font-size: 140px;
    line-height: 1;
  }
  .author-main {
    position: absolute;
    left: 0; width: 100%;
    top: 1030px;
    text-align: center;
    font-weight: 500;
    font-size: 39px;
    color: var(--royal-blue);
    letter-spacing: 0.01em;
  }
  .author-second {
    position: absolute;
    left: 0; width: 100%;
    top: 1082px;
    text-align: center;
    font-weight: 500;
    font-size: 29px;
    letter-spacing: 0.12em;
  }
  .author-second .joiner {
    font-size: 21px;
    letter-spacing: 0;
    margin-right: 6px;
  }
</style>
</head>
<body>
  <main class="cover">
    <div class="title-row" style="top:81px">
      <svg class="eye-art" role="img" aria-label="Illustration of an eyeball with a small surgical instrument" viewBox="0 0 118 118"><circle cx="59" cy="59" r="58" fill="var(--ink-light)"/></svg>
      <span class="title-word">Three</span>
    </div>
    <div class="subtitle-line" style="top:233px">Quiet Pointers</div>

    <div class="title-row" style="top:280px">
      <span class="title-word">Lamps</span>
    </div>
    <div class="subtitle-line" style="top:431px">For Picking a</div>

    <div class="title-row" style="top:476px">
      <svg class="eye-art" role="img" aria-label="Illustration of an eyeball with a small surgical instrument" viewBox="0 0 118 118"><circle cx="59" cy="59" r="58" fill="var(--ink-light)"/></svg>
      <span class="title-word">At</span>
    </div>
    <div class="subtitle-line" style="top:629px">Trustworthy</div>

    <div class="title-row" style="top:680px">
      <span class="title-word">Dusk</span>
      <svg class="eye-art" role="img" aria-label="Illustration of an eyeball with a small surgical instrument" viewBox="0 0 118 118"><circle cx="59" cy="59" r="58" fill="var(--ink-light)"/></svg>
    </div>
    <div class="subtitle-line accent" style="top:839px">Retina Practitioner</div>

    <div class="question-mark">?</div>

    <div class="author-main">DEREK H. TOLLAND, MD</div>
    <div class="author-second"><span class="joiner">and</span>GLEN T. ASHWORTH</div>
  </main>
</body>
</html>
```